Bright Path Mission- a non profit locin TZ , east Africa. Needing to attract donors.

A flyer for donors /potential partners. showing what their giving has accomplished this year. An Encouraging way to say thank you at the same time informing the partner of the amazing things God is doing with their generous, faithful giving. We will need to print/email. Thank you for considering this project. Your efforts help in educating and feeding 225 street children, providing a safe haven and trade school for hundreds of women and abused teenagers, medical ship on the longest lake in the world going into unreached people groups, a Bible College Training up pastors to plant churches all over TZ, Congo, Burundi and beyond, youth and children’s kids clubs and youth camps. These are the main areas of bright path mission. Bible college, primary school, trade schools, youth camps/kids clubs. We need help in making sure readers will be drawn to seeing/reading more which leads to donations without overwhelming with too much info. HELP! I can tell you about Jesus I have even authored 7 books, but making s flyer that makes sense it out of my wheelhouse. Again, thank you.
Updates

I do not want longer I need quicker and paid for a 3 day quote. All pictures and logo are on our website. I have tried to send pictures but they won’t send. Please look at. Www.brightpathmissiontz.org

Target Market(s)

Professional adults, large companies, donors

Industry/Entity Type

Non profit missionary Bright Path Mission in Tanzania, Congo, USA and soon to be Canada.

Requirements
Must have
• Color professional pictures, feel good, exciting want to be apart of what God is doing
Nice to have
• Glossy trifold
Should not have
• Fly in the face, guilt feeling, animals in Africa

```html
<!DOCTYPE html>
<html lang="en">
<head>
<meta charset="utf-8">
<title>Bright Path Mission – Partner Flyer</title>
<link rel="stylesheet" href="https://fonts.googleapis.com/css2?family=Montserrat:wght@400;500;600;700;800;900&display=swap">
<style>
:root{
  --ink:#16170f;
  --green:#4dbb63;
  --green-dark:#2f9e48;
  --lime:#b6d98a;
  --cream:#e8e9b4;
  --paper:#f6f6f8;
  --text:#2a2a2a;
  --stage:#e6e7eb;
  --heart:#c8102e;
}
*{box-sizing:border-box;margin:0;padding:0}
html,body{width:956px;height:1200px;overflow:hidden;background:var(--stage);font-family:"Montserrat",sans-serif;color:var(--text)}
.flyer{position:absolute;left:53px;top:0;width:849px;height:1200px;background:var(--paper);overflow:hidden}
.abs{position:absolute}

/* left column */
.brand-block{left:0;top:0;width:336px;height:226px;background:var(--ink);display:flex;align-items:center;justify-content:center}
.brand-name{font-weight:800;font-size:30px;line-height:1.05;color:var(--lime);text-align:center;letter-spacing:1px}
.pill{border:2px solid var(--green);border-radius:8px;background:#fff;font-size:24px;font-weight:500;color:var(--ink);padding:0 18px;display:flex;align-items:center;height:38px;white-space:nowrap}
.pill b{color:var(--green);font-weight:700;margin-left:8px}
.serve-pill{left:38px;top:248px;width:270px}
.serve-list{left:40px;top:302px;list-style:none}
.serve-list li{display:flex;align-items:center;height:29px;font-size:17px;font-weight:700;letter-spacing:.5px;color:var(--ink)}
.serve-list svg{width:14px;height:14px;margin-right:22px}
.help-pill{left:38px;top:483px;width:234px}
.help-copy{left:41px;top:533px;width:272px;font-size:11.5px;line-height:15.2px;color:#333}
.photo-a{left:41px;top:708px;width:103px;height:106px;background:linear-gradient(135deg,#e8c0a8,#8b5a45 55%,#c23030)}
.photo-b{left:185px;top:708px;width:106px;height:106px;background:linear-gradient(160deg,#b7cbe0,#8c6a48 55%,#3d5a92)}
.photo-c{left:41px;top:848px;width:103px;height:104px;background:linear-gradient(160deg,#c9d6d8,#7b6250 55%,#c0704b)}
.photo-d{left:185px;top:848px;width:106px;height:104px;background:linear-gradient(140deg,#e6e8ee,#5b4337 55%,#3f6fb0)}
.grid-lines{left:41px;top:708px;width:250px;height:244px}
.donate-badge{left:128px;top:786px;width:76px;height:76px;border-radius:50%;background:var(--heart);border:3px solid #fff;color:#fff;display:flex;flex-direction:column;align-items:center;justify-content:center;font-weight:800;font-size:13px;line-height:1.05}
.quote{left:41px;top:970px;width:290px;font-size:17.5px;font-weight:800;line-height:22px;color:var(--ink)}
.quote span{display:block;color:var(--green);font-size:16px}
.thanks-block{left:0;top:1054px;width:336px;height:146px;background:var(--ink);border-top-right-radius:18px;padding:18px 40px 0 40px}
.thanks-title{font-size:19px;font-weight:700;line-height:24px;color:var(--green)}
.thanks-copy{margin-top:14px;font-size:11.5px;line-height:14px;color:#fff}

/* right column */
.accent-stripe{left:336px;top:0;width:26px;height:700px;background:linear-gradient(var(--lime),var(--green))}
.title-block{left:360px;top:0;width:489px;height:226px;background:var(--ink);padding:22px 30px 0 32px}
.title{font-size:44px;font-weight:900;line-height:49px;color:#fff;letter-spacing:.5px}
.subtitle{margin-top:14px;border-top:1.5px solid var(--cream);border-bottom:1.5px solid var(--cream);padding:6px 0 5px;font-size:17.5px;line-height:24px;font-weight:500;color:var(--cream);width:412px}
.hero{left:360px;top:226px;width:489px;height:419px;background:radial-gradient(ellipse at 55% 45%,#c6a07f,#6e5645 45%,#2f2a28 85%)}
.partner-block{left:336px;top:645px;width:513px;height:161px;background:linear-gradient(90deg,var(--green),var(--lime));border-bottom-left-radius:16px}
.heart{left:32px;top:30px;width:50px;height:45px}
.partner-title{left:100px;top:20px;font-size:27px;line-height:30px;color:var(--ink);font-weight:500}
.partner-title b{font-weight:800}
.partner-divider{left:277px;top:18px;width:1.5px;height:72px;background:var(--ink)}
.partner-copy{left:294px;top:20px;width:206px;font-size:12.5px;line-height:17px;color:var(--ink)}
.donate-url{left:33px;top:108px;width:438px;height:38px;border:2px solid var(--ink);display:flex;align-items:center;justify-content:center;font-size:18px;font-weight:600;letter-spacing:1.8px;color:var(--ink)}
.icon{width:40px;height:40px}
.serve-icon{left:362px;top:832px}
.teacher-icon{left:362px;top:997px}
.serve2-pill{left:399px;top:825px;width:253px}
.serve-copy{left:399px;top:880px;width:410px;font-size:11.5px;line-height:14.5px;color:#333}
.teacher-pill{left:399px;top:991px;width:407px}
.teacher-copy{left:401px;top:1040px;width:400px;font-size:11.5px;line-height:14.5px;color:#333}
.contact-band{left:315px;top:1087px;width:534px;height:113px;background:var(--green);border-top-left-radius:4px}
.contact-title{left:22px;top:18px;font-size:24px;font-weight:800;color:var(--ink);letter-spacing:.5px}
.contact-rule{left:22px;top:50px;width:220px;height:8px}
.contact-legal{left:22px;top:62px;font-size:8.5px;line-height:11px;font-weight:600;color:var(--ink);text-transform:uppercase}
.contact-line{left:282px;display:flex;align-items:center;font-size:10.5px;font-weight:700;line-height:13px;color:var(--ink);text-transform:uppercase}
.contact-line svg{width:15px;height:15px;margin-right:18px}
.contact-mail{top:22px}
.contact-web{top:68px}
</style>
</head>
<body>
<main class="flyer">
  <!-- left column -->
  <header class="abs brand-block"><div class="brand-name">BRIGHT PATH<br>MISSION</div></header>

  <div class="abs pill serve-pill">WHAT<b>WE SERVE</b></div>
  <ul class="abs serve-list">
    <li><svg viewBox="0 0 14 14"><circle cx="7" cy="7" r="6" fill="none" stroke="#16170f" stroke-width="1.3"/><path d="M4 7.2l2 2 4-4" fill="none" stroke="#16170f" stroke-width="1.3"/></svg>BIBLE COLLEGE</li>
    <li><svg viewBox="0 0 14 14"><circle cx="7" cy="7" r="6" fill="none" stroke="#16170f" stroke-width="1.3"/><path d="M4 7.2l2 2 4-4" fill="none" stroke="#16170f" stroke-width="1.3"/></svg>PRE PRIMARY SCHOOL</li>
    <li><svg viewBox="0 0 14 14"><circle cx="7" cy="7" r="6" fill="none" stroke="#16170f" stroke-width="1.3"/><path d="M4 7.2l2 2 4-4" fill="none" stroke="#16170f" stroke-width="1.3"/></svg>KIDS CLUBS</li>
    <li><svg viewBox="0 0 14 14"><circle cx="7" cy="7" r="6" fill="none" stroke="#16170f" stroke-width="1.3"/><path d="M4 7.2l2 2 4-4" fill="none" stroke="#16170f" stroke-width="1.3"/></svg>VILLAGE OUTREACH</li>
    <li><svg viewBox="0 0 14 14"><circle cx="7" cy="7" r="6" fill="none" stroke="#16170f" stroke-width="1.3"/><path d="M4 7.2l2 2 4-4" fill="none" stroke="#16170f" stroke-width="1.3"/></svg>TEAM OUTREACH</li>
    <li><svg viewBox="0 0 14 14"><circle cx="7" cy="7" r="6" fill="none" stroke="#16170f" stroke-width="1.3"/><path d="M4 7.2l2 2 4-4" fill="none" stroke="#16170f" stroke-width="1.3"/></svg>MICRO BUSINESSES</li>
  </ul>

  <div class="abs pill help-pill">HOW<b>WE HELP</b></div>
  <p class="abs help-copy">Your efforts help in educating and feeding 225 street children, providing a safe haven and trade school for hundreds of women and abused teenagers, medical ship on the longest lake in the world going into unreached people groups, Bible College Training up pastors to plant churches all over TZ, Congo, Burundi and beyond, youth and children's kids clubs and youth camps.</p>

  <div class="abs photo-a" role="img" aria-label="Photo of a missionary smiling with a child"></div>
  <div class="abs photo-b" role="img" aria-label="Photo of a group of children gathered outdoors"></div>
  <div class="abs photo-c" role="img" aria-label="Photo of two people standing together in a village"></div>
  <div class="abs photo-d" role="img" aria-label="Photo of children studying with books at a desk"></div>
  <svg class="abs grid-lines" viewBox="0 0 250 244"><path d="M0 122H250M125 0V244" stroke="#bfc0c4" stroke-width="1.5"/></svg>
  <div class="abs donate-badge"><span>DONATE</span><span>NOW</span></div>

  <blockquote class="abs quote">"IN HIS NAME THE NATIONS WILL PUT THEIR HOPE."<span>MT. 12:21</span></blockquote>

  <footer class="abs thanks-block">
    <h3 class="thanks-title">THANK YOU FOR<br>YOUR DONATIONS</h3>
    <p class="thanks-copy">Partnering of the amazing things God is doing with their generous, faithful giving.</p>
  </footer>

  <!-- right column -->
  <div class="abs accent-stripe"></div>
  <section class="abs title-block">
    <h1 class="title">TO BRING HOPE<br>TO THE NATIONS</h1>
    <p class="subtitle">THROUGH THE KNOWLEDGE OF JESUS CHRIST AND THE WORD OF GOD.</p>
  </section>
  <div class="abs hero" role="img" aria-label="Photo of smiling schoolchildren in a classroom, one holding up a small chalkboard"></div>

  <section class="abs partner-block">
    <svg class="abs heart" viewBox="0 0 58 52"><path d="M29 50C12 38 2 28 2 16 2 7 9 2 16 2c6 0 10 3 13 8 3-5 7-8 13-8 7 0 14 5 14 14 0 12-10 22-27 34z" fill="#c8102e"/></svg>
    <h2 class="abs partner-title"><b>PARTNER</b><br>WITH US</h2>
    <div class="abs partner-divider"></div>
    <p class="abs partner-copy">By partnering with Bright Path Mission, you are never simply a "sponsor" or "donor".</p>
    <div class="abs donate-url">BRIGHTPATHMISSIONTZ.ORG/DONATE</div>
  </section>

  <svg class="abs icon serve-icon" viewBox="0 0 40 40" fill="none" stroke="#555" stroke-width="1.6"><circle cx="22" cy="9" r="4"/><path d="M22 1v3M22 14v3M14 9h3M27 9h3"/><path d="M3 33l7-7c2-2 5-2 7-1l6 2c2 1 1 4-1 4h-7M16 31h10l9-7c2-1 3 1 2 3l-9 8H12l-5 4"/></svg>
  <div class="abs pill serve2-pill">HOW<b>WE SERVE</b></div>
  <p class="abs serve-copy">Our vision is to raise up a generation of godly influencers. These are young people who are firmly grounded in their relationship with Jesus Christ. They have received the besteducation, enabling them to take up positions of influence in every area of their nation. We started with a preschool, which over the years grew into a primary school with over 200 students.</p>

  <svg class="abs icon teacher-icon" viewBox="0 0 40 40" fill="none" stroke="#555" stroke-width="1.8"><circle cx="20" cy="10" r="7"/><path d="M5 38v-8c0-5 5-9 15-9s15 4 15 9v8z"/><path d="M20 21l-3 6 3 4 3-4z"/></svg>
  <div class="abs pill teacher-pill">ARE YOU<b>A BIBLE TEACHER?</b></div>
  <p class="abs teacher-copy">We depend on visiting pastors / Bible teachers. Come make an impact on students who hunger to learn God's word.</p>

  <footer class="abs contact-band">
    <h3 class="abs contact-title">CONTACT US</h3>
    <svg class="abs contact-rule" viewBox="0 0 220 8"><path d="M0 4H214" stroke="#16170f" stroke-width="1.5"/><circle cx="215" cy="4" r="3.5" fill="#16170f"/></svg>
    <p class="abs contact-legal">Bright Path Mission is a 501c(3)<br>non-profit corporation.<br>Federal Tax ID # 47-2019384</p>
    <p class="abs contact-line contact-mail"><svg viewBox="0 0 15 15" fill="none" stroke="#16170f" stroke-width="1.2"><circle cx="7.5" cy="7.5" r="6.5"/><ellipse cx="7.5" cy="7.5" rx="3" ry="6.5"/><path d="M1 7.5h13"/></svg>PO BOX 2480<br>MILLBROOK, CA 95612</p>
    <p class="abs contact-line contact-web"><svg viewBox="0 0 15 15"><path d="M7.5 14C5 10 3.5 8 3.5 5.5a4 4 0 018 0C11.5 8 10 10 7.5 14z" fill="#16170f"/><circle cx="7.5" cy="5.5" r="1.5" fill="#4dbb63"/></svg>BRIGHTPATHMISSIONTZ.ORG</p>
  </footer>
</main>
</body>
</html>
```